Business Card Design

Electronic Security Installation Specialists

Check out our website at www.brightpulsellc.com to see what we do.

Industry/Entity Type

Business

Contact Information for Business Card

Bright Pulse
Marianne Tolbert
218 Orchard Bend
Millbrook, OR 97310

Colors
3176b5
0455a3
ffffff

```html
<!DOCTYPE html>
<html lang="en">
<head>
<meta charset="utf-8">
<title>Bright Pulse – Business Card</title>
<link rel="stylesheet" href="https://fonts.googleapis.com/css2?family=Exo+2:wght@700&family=Didact+Gothic&display=swap">
<style>
  :root {
    --brand-light: #3176b5;
    --brand-deep: #0455a3;
    --white: #ffffff;
    --ink: #1b1b1b;
    --metal-hi: #f4f4f4;
    --metal-mid: #d9d9d9;
    --metal-lo: #bdbdbd;
    --backdrop: #e7e4df;
  }
  * { box-sizing: border-box; margin: 0; padding: 0; }
  html, body {
    width: 1200px;
    height: 900px;
    overflow: hidden;
    background: var(--backdrop);
  }
  .canvas {
    width: 1200px;
    height: 900px;
    display: flex;
    flex-direction: column;
    align-items: center;
    justify-content: center;
    gap: 60px;
  }
  .card {
    position: relative;
    width: 630px;
    height: 360px;
    border-radius: 2px;
    background:
      repeating-linear-gradient(0deg, rgba(255,255,255,0.35) 0 1px, rgba(0,0,0,0.04) 1px 3px),
      linear-gradient(160deg, var(--metal-hi) 0%, var(--metal-mid) 45%, var(--metal-hi) 70%, var(--metal-lo) 100%);
    box-shadow: 0 10px 24px rgba(0,0,0,0.25);
    overflow: hidden;
  }
  .brand {
    display: flex;
    align-items: center;
    gap: 14px;
  }
  .brand-dot {
    width: 34px;
    height: 34px;
    border-radius: 50%;
    background: var(--brand-light);
    flex: none;
  }
  .brand-name {
    font-family: "Exo 2", sans-serif;
    font-weight: 700;
    font-size: 38px;
    color: var(--brand-light);
    white-space: nowrap;
  }
  .card-front {
    display: flex;
    align-items: center;
    justify-content: center;
  }
  .card-back .brand {
    position: absolute;
    left: 40px;
    top: 118px;
  }
  .card-back .brand-dot { background: var(--brand-deep); width: 28px; height: 28px; }
  .card-back .brand-name { color: var(--brand-deep); font-size: 30px; }
  .divider {
    position: absolute;
    left: 340px;
    top: 70px;
    width: 2px;
    height: 110px;
    background: var(--ink);
  }
  .holder-name {
    position: absolute;
    left: 372px;
    top: 100px;
    font-family: "Exo 2", sans-serif;
    font-weight: 700;
    font-size: 19px;
    color: var(--ink);
    white-space: nowrap;
  }
  .address {
    position: absolute;
    left: 0;
    right: 0;
    bottom: 52px;
    text-align: center;
    font-family: "Didact Gothic", sans-serif;
    font-size: 15px;
    color: var(--ink);
    white-space: nowrap;
  }
</style>
</head>
<body>
  <main class="canvas">
    <section class="card card-front" aria-label="Card front">
      <div class="brand">
        <span class="brand-dot"></span>
        <span class="brand-name">Bright Pulse</span>
      </div>
    </section>
    <section class="card card-back" aria-label="Card back">
      <div class="brand">
        <span class="brand-dot"></span>
        <span class="brand-name">Bright Pulse</span>
      </div>
      <span class="divider"></span>
      <p class="holder-name">Marianne Tolbert</p>
      <p class="address">218 Orchard Bend Millbrook, OR 97310</p>
    </section>
  </main>
</body>
</html>
```